Kem7Dex Letterhead

Need a new letterhead for my law firm.
IDENTIFYING INFORMATION BELOW:
Ansel T Brightwater III
Attorney at Law
Address: 4832 Tillbury Rd, Ste 250, Dallas, TX 75204
Phone: 866-402-7183
Fax: 469-583-0271
Email: kem@kem7dex.example
Website: www.kem7dex.example

Colors
0054AA
0677BA
7BADD7
CADEEF
E8F1F8

Requirements
Must have
• Logo needs to be on the letterhead, along with identifying information which is included in the project description.

```html
<!DOCTYPE html>
<html lang="en">
<head>
<meta charset="utf-8">
<title>Kem7Dex Letterhead</title>
<link href="https://fonts.googleapis.com/css2?family=Roboto:wght@300;400;700;900&family=Great+Vibes&display=swap" rel="stylesheet">
<style>
  :root {
    --brand-blue: #0054AA;
    --brand-mid: #0677BA;
    --ink: #1c1c1c;
    --body-ink: #2a2a2a;
    --paper: #f3f3f3;
    --backdrop: #e4e4e4;
  }
  * { margin: 0; padding: 0; box-sizing: border-box; }
  html, body {
    width: 1200px; height: 1200px; overflow: hidden;
    background: var(--backdrop);
    font-family: "Roboto", "Helvetica Neue", Arial, sans-serif;
  }
  .letterhead {
    position: absolute; left: 197px; top: 30px;
    width: 806px; height: 1140px;
    background: var(--paper);
    box-shadow: 0 4px 18px rgba(0,0,0,0.12);
    color: var(--body-ink);
  }
  .brand-name {
    position: absolute; left: 78px; top: 60px;
    font-weight: 900; font-size: 32px; letter-spacing: 2px;
    color: var(--ink); line-height: 1;
  }
  .attorney {
    position: absolute; left: 570px; top: 71px;
    border-left: 3px solid var(--brand-blue);
    padding-left: 14px; font-size: 13.5px; line-height: 17px;
  }
  .attorney-name { color: var(--brand-blue); font-weight: 700; }
  .attorney-title { color: var(--ink); font-weight: 400; }
  .letter { position: absolute; left: 86px; width: 634px; font-weight: 300; font-size: 13.4px; line-height: 19px; color: var(--body-ink); }
  .letter-date { top: 258px; }
  .letter-recipient { top: 296px; }
  .letter-greeting { top: 391px; }
  .letter-body { top: 429px; text-align: justify; }
  .letter-body p + p { margin-top: 19px; }
  .letter-closing { top: 845px; }
  .signature {
    position: absolute; left: 88px; top: 866px;
    font-family: "Great Vibes", cursive; font-size: 28px; color: var(--ink);
  }
  .contact {
    position: absolute; top: 1041px; font-size: 13.5px; line-height: 16.5px; color: var(--ink); font-weight: 400;
    white-space: nowrap;
  }
  .contact-lines { left: 75px; }
  .contact-line { display: flex; align-items: center; gap: 6px; }
  .contact-line svg { width: 11px; height: 11px; fill: var(--brand-blue); flex: none; }
  .contact-address { left: 262px; top: 1057.5px; }
  .contact-web { left: auto; right: 78px; top: 1074px; color: var(--brand-mid); }
  .footer-band {
    position: absolute; left: 0; bottom: 0; width: 100%; height: 10px;
    background: var(--brand-blue);
  }
</style>
</head>
<body>
<main class="letterhead">
  <div class="brand-name">KEM7DEX</div>

  <div class="attorney">
    <div class="attorney-name">Ansel T Brightwater III</div>
    <div class="attorney-title">Attorney at Law</div>
  </div>

  <div class="letter letter-date">01 January 2050</div>
  <div class="letter letter-recipient">Company (Pvt) Ltd.<br>PO Box 3355 Mainville St<br>Sample City Country 3355</div>
  <div class="letter letter-greeting">Dear Dana Whitcombe,</div>

  <div class="letter letter-body">
    <p>Lorem ipsum dolor sit amet, consectetuer adipiscing elit, sed diam nonummy nibh euismod tincidunt ut laoreet dolore magna aliquam erat volutpat. Ut wisi enim ad minim veniam, quis nostrud exerci tation ullamcorper suscipit lobortis nisl ut aliquip ex ea commodo consequat. Duis dolore te feugait nulla facilisi. Nam liber tempor cum soluta nobis eleifend option congue nihil imperdiet doming id quod mazim placerat facer possim assum. Lorem ipsum dolor sit amet, consectetuer adipiscing elit, sed diam nonummy nibh euismod tincidunt ut laoreet dolore magna aliquam erat volutpat. Ut wisi enim ad minim veniam, quis nostrud exerci tation ullamcorper suscipit lobortis nisl ut aliquip ex ea commodo consequat.</p>
    <p>Consectetuer adipiscing elit, sed diam nonummy nibh euismod tincidunt ut laoreet dolore magna aliquam erat volutpat. Ut wisi enim ad minim veniam, quis nostrud exerci tation ullamcorper suscipit lobortis nisl ut aliquip ex ea commodo consequat. Consectetuer adipiscing elit, sed diam nonummy nibh euismod tincidunt ut laoreet dolore magna aliquam erat volutpat. Ut wisi enim ad minim veniam, quis nostrud exerci tation ullamcorper suscipit lobortis nisl ut aliquip ex ea commodo consequat.</p>
    <p>Consectetuer adipiscing elit, sed diam nonummy nibh euismod tincidunt ut laoreet dolore magna aliquam erat volutpat. Ut wisi enim ad minim veniam, quis nostrud exerci tation ullamcorper suscipit lobortis nisl ut aliquip ex ea commodo consequat. Consectetuer adipiscing elit, sed diam nonummy nibh euismod tincidunt ut laoreet dolore magna aliquam erat volutpat. Ut wisi enim ad minim veniam, quis nostrud exerci tation ullamcorper suscipit lobortis nisl ut aliquip ex ea commodo consequat.</p>
  </div>

  <div class="letter letter-closing">Sincerely Yours</div>
  <div class="signature">Marcus Ellery</div>

  <div class="contact contact-lines">
    <div class="contact-line">
      <svg viewBox="0 0 24 24" aria-hidden="true"><path d="M6.6 10.8a15 15 0 0 0 6.6 6.6l2.2-2.2c.3-.3.7-.4 1-.2 1.1.4 2.3.6 3.6.6.6 0 1 .4 1 1V20c0 .6-.4 1-1 1A17 17 0 0 1 3 4c0-.6.4-1 1-1h3.5c.6 0 1 .4 1 1 0 1.3.2 2.5.6 3.6.1.3 0 .7-.2 1z"/></svg>
      <span>866-402-7183</span>
    </div>
    <div class="contact-line">
      <svg viewBox="0 0 24 24" aria-hidden="true"><path d="M6 2h10l2 2v5H6zM3 10h18a1 1 0 0 1 1 1v7h-4v4H6v-4H2v-7a1 1 0 0 1 1-1zm5 7v3h8v-3z"/></svg>
      <span>469-583-0271</span>
    </div>
    <div class="contact-line">
      <svg viewBox="0 0 24 24" aria-hidden="true"><path d="M2 5h20v14H2zm2 2v.5l8 5.5 8-5.5V7l-8 5.5z"/></svg>
      <span>kem@kem7dex.example</span>
    </div>
  </div>
  <div class="contact contact-address">4832 Tillbury Rd<br>Ste 250, Dallas, TX 75204</div>
  <div class="contact contact-web">www.kem7dex.example</div>

  <div class="footer-band"></div>
</main>
</body>
</html>
```